Tarvel Ridge LLC

Need Professional Business cards for New Investment Fund

Target Market(s)

High Quality investors

Industry/Entity Type

Financial

Contact Information for Business Card

Phone Number +1 555 284 6193
Name Pavel Orlinsky
Title Fund Manager
email po@FundTarvel.example
Website www.FundTarvel.example

Colors

Designer to choose colors to be used in the design.

Requirements
Must have
• Must have our Logo and all of the above. Must be made so lettering and loge can be raised

```html
<!DOCTYPE html>
<html lang="en">
<head>
<meta charset="UTF-8">
<title>Tarvel Ridge LLC – Business Card</title>
<link rel="stylesheet" href="https://fonts.googleapis.com/css2?family=Jost:wght@400;500;600&family=Poppins:wght@400&display=swap">
<style>
  :root {
    --bg: #2b2f35;
    --green: #56b843;
    --green-deep: #4a8a3f;
    --green-dark: #40573f;
    --charcoal: #3f4a40;
    --ink: #2f3a31;
    --paper: #ffffff;
  }
  * { margin: 0; padding: 0; box-sizing: border-box; }
  html, body { width: 1200px; height: 1000px; overflow: hidden; }
  body {
    background: var(--bg);
    display: flex;
    flex-direction: column;
    align-items: center;
    justify-content: center;
    gap: 50px;
    font-family: "Jost", sans-serif;
  }
  .card {
    width: 840px;
    height: 420px;
    border-radius: 26px;
    position: relative;
    overflow: hidden;
  }
  .card-front {
    background: linear-gradient(100deg, var(--green) 0%, var(--green-deep) 45%, var(--green-dark) 100%);
    display: flex;
    align-items: center;
    justify-content: center;
  }
  .brand-mark {
    display: flex;
    align-items: center;
    gap: 16px;
  }
  .brand-mark .dot {
    width: 22px;
    height: 22px;
  }
  .brand-name {
    font-weight: 500;
    letter-spacing: 4px;
    text-transform: uppercase;
  }
  .card-front .dot { background: var(--paper); }
  .card-front .brand-name { color: var(--paper); font-size: 54px; }

  .card-back { background: var(--paper); }
  .details {
    position: absolute;
    left: 64px;
    top: 58px;
  }
  .company {
    font-weight: 600;
    font-size: 34px;
    line-height: 1;
    text-transform: uppercase;
    color: var(--ink);
  }
  .company .accent { color: var(--green); }
  .tagline {
    margin-top: 8px;
    color: var(--green);
    font-size: 17px;
    letter-spacing: 12px;
    text-transform: uppercase;
  }
  .person { margin-top: 52px; }
  .person-name {
    font-weight: 600;
    font-size: 26px;
    text-transform: uppercase;
    color: var(--ink);
  }
  .person-title {
    color: var(--green);
    font-size: 17px;
    letter-spacing: 10px;
    text-transform: uppercase;
    margin-top: 2px;
  }
  .contacts {
    list-style: none;
    margin-top: 22px;
    font-family: "Poppins", sans-serif;
    font-size: 19px;
    color: var(--ink);
  }
  .contacts li {
    display: flex;
    align-items: center;
    gap: 12px;
    height: 30px;
  }
  .contacts svg { width: 18px; height: 18px; fill: var(--green); flex: none; }
  .card-back .brand-mark {
    position: absolute;
    right: 70px;
    top: 50%;
    transform: translateY(-50%);
  }
  .card-back .dot { background: var(--green); width: 26px; height: 26px; }
  .card-back .brand-name { color: var(--charcoal); font-size: 64px; }
</style>
</head>
<body>
  <section class="card card-front">
    <div class="brand-mark">
      <span class="dot"></span>
      <span class="brand-name">Tarvel</span>
    </div>
  </section>

  <section class="card card-back">
    <div class="details">
      <h1 class="company"><span class="accent">Tarvel</span> Ridge LLC</h1>
      <p class="tagline">Investment Fund</p>
      <div class="person">
        <h2 class="person-name">Pavel Orlinsky</h2>
        <p class="person-title">Fund Manager</p>
      </div>
      <ul class="contacts">
        <li>
          <svg viewBox="0 0 24 24" aria-hidden="true"><path d="M6.6 10.8a15.1 15.1 0 0 0 6.6 6.6l2.2-2.2a1 1 0 0 1 1-.25 11.4 11.4 0 0 0 3.6.57 1 1 0 0 1 1 1V20a1 1 0 0 1-1 1A17 17 0 0 1 3 4a1 1 0 0 1 1-1h3.5a1 1 0 0 1 1 1c0 1.25.2 2.45.57 3.6a1 1 0 0 1-.25 1z"/></svg>
          +1 555 284 6193
        </li>
        <li>
          <svg viewBox="0 0 24 24" aria-hidden="true"><path d="M2 5h20v14H2z M2 5l10 8 10-8" stroke="#fff" stroke-width="1.5"/></svg>
          po@FundTarvel.example
        </li>
        <li>
          <svg viewBox="0 0 24 24" aria-hidden="true"><circle cx="12" cy="12" r="10"/><path d="M2 12h20M12 2c3 3 3 17 0 20M12 2c-3 3-3 17 0 20M4 7h16M4 17h16" stroke="#fff" stroke-width="1.2" fill="none"/></svg>
          www.FundTarvel.example
        </li>
      </ul>
    </div>
    <div class="brand-mark">
      <span class="dot"></span>
      <span class="brand-name">Tarvel</span>
    </div>
  </section>
</body>
</html>
```